Flyer-Design für Aktionstag einer Teddy-Klinik gesucht
Zielgruppe
Ursprünglich ist die Teddyklinik eine Idee aus Schweden, doch inzwischen haben Fach-schaften in Deutschland an vielen medizinischen Universitäten diese Idee aufgenommen und umgesetzt. Seit einigen Jahren gibt es die Teddyklinik auch an der Universität zu Harvelsund, als AG der Fachschaft Medizin.
Aufgabenstellung
siehe Briefing-Dokument

```html
<!DOCTYPE html>
<html lang="de">
<head>
<meta charset="utf-8">
<title>Teddyklinik Flyer</title>
<link href="https://fonts.googleapis.com/css2?family=Source+Sans+3:wght@400;600;700&display=swap" rel="stylesheet">
<style>
  :root {
    --backdrop: #eef1f2;
    --paper: #ffffff;
    --brand-ink: #1f4a5a;
    --band-dark: #4c7486;
    --band-light: #7c9ba9;
    --band-dark-sub: #d3e0e6;
    --url-tone: #b9cdd5;
    --white: #ffffff;
  }
  * { box-sizing: border-box; margin: 0; padding: 0; }
  html, body {
    width: 1200px; height: 759px; overflow: hidden;
    background: var(--backdrop);
    font-family: "Source Sans 3", "Myriad Pro", Arial, sans-serif;
  }
  .canvas {
    width: 1200px; height: 759px;
    display: flex; align-items: center; justify-content: center;
  }
  .flyer {
    width: 336px; height: 720px;
    background: var(--paper);
    box-shadow: 4px 5px 10px rgba(0,0,0,0.22);
    position: relative;
    padding: 0 27px;
  }
  .brand {
    height: 116px;
    display: flex; align-items: center; gap: 9px;
  }
  .brand-dot {
    width: 54px; height: 54px; border-radius: 50%;
    border: 2px solid var(--brand-ink);
    flex: none;
  }
  .brand-name {
    color: var(--brand-ink);
    font-weight: 700; font-size: 9.2px; letter-spacing: 1.4px;
    text-transform: uppercase;
  }
  .hero {
    position: relative;
    height: 388px;
    background:
      radial-gradient(ellipse at 35% 45%, rgba(236,226,222,0.9) 0%, rgba(236,226,222,0) 55%),
      radial-gradient(ellipse at 85% 70%, rgba(236,180,196,0.75) 0%, rgba(236,180,196,0) 45%),
      radial-gradient(ellipse at 30% 95%, rgba(80,140,200,0.7) 0%, rgba(80,140,200,0) 45%),
      linear-gradient(180deg, #eceae8 0%, #e4dfdc 55%, #c9c7cf 100%);
    overflow: hidden;
  }
  .hero-title {
    position: absolute; left: 0; right: 0; bottom: 18px;
    text-align: center;
    color: var(--white);
    font-weight: 700; font-size: 42px; letter-spacing: -0.3px;
    text-shadow: 0 1px 4px rgba(0,0,0,0.35);
  }
  .event-band {
    height: 66px;
    background: var(--band-dark);
    color: var(--white);
    text-align: center;
    padding-top: 10px;
  }
  .event-date { font-weight: 700; font-size: 18.5px; line-height: 1.15; }
  .event-place {
    font-weight: 600; font-size: 13.4px; color: var(--band-dark-sub);
    text-transform: uppercase; margin-top: 2px;
  }
  .info-band {
    height: 122px;
    background: var(--band-light);
    color: var(--white);
    text-align: center;
    padding: 15px 20px 0;
  }
  .info-text { font-size: 9.6px; line-height: 1.35; }
  .info-note { font-weight: 700; font-size: 9.6px; margin-top: 10px; }
  .info-url {
    font-weight: 700; font-size: 11.6px; color: var(--url-tone);
    margin-top: 11px;
  }
</style>
</head>
<body>
  <main class="canvas">
    <article class="flyer">
      <header class="brand">
        <span class="brand-dot"></span>
        <span class="brand-name">Universität zu Harvelsund</span>
      </header>

      <section class="hero" role="img" aria-label="Foto: Ärztin mit Stethoskop untersucht gemeinsam mit einem Mädchen einen weißen Teddybären">
        <h1 class="hero-title">Teddyklinik</h1>
      </section>

      <section class="event-band">
        <p class="event-date">22.06.2019 I 10.00-16.00 Uhr</p>
        <p class="event-place">Marktplatz am Rathaus in Harvelsund</p>
      </section>

      <section class="info-band">
        <p class="info-text">Am Aktionstag werden wir die<br>Lieblingsstofftiere der Kinder „behandeln“ und sie<br>als Teddy-Eltern mit in alle Abläufe einbeziehen.</p>
        <p class="info-note">Keine Voranmeldung nötig! Kostenlos!</p>
        <p class="info-url">www.teddyklinik.uni-harvelsund.de</p>
      </section>
    </article>
  </main>
</body>
</html>
```